VESTRA電子書籍 表紙発注書

【依頼概要】

<サブタイトル>

小さな会社や個人事業でもできる!

<書籍タイトル>

数字が苦手な 店主のための
【看板づくり手帖】

※ターゲットの目にすぐ入る様に(小さな会社)(個人事業)(ネットに弱い)を目立つ様にお願いします。
※電子書籍なので表示される際の画像が小さいため、タイトルもできるだけ視認しやすい文字でお願いします。

<オビ部分>

ホームページを作る前に
必ずお読みください。

読者限定プレゼント付
●思わずポチッと押したくなる!
【段階別】キャッチコピーの作り方
●真似するだけでOK!
【ランディングページのテンプレート】

※プレゼントは目立つ様にお願いします。

<著者>

WEB集客のしくみ作りの専門家
森田 サキ

※著者似顔絵をどちらか使ってください。

<読者ターゲット層>
・40代~50代の、小規模企業の経営者・個人事業経営者・個人起業家

<イメージ>
・色の指定などはありません。
もし自分が起業する時なら、どんな表紙に目が止まるか考えてみていただけると嬉しいです。

・ビジネス書ではありますが、ターゲットはネットやパソコンに苦手意識を持っている経営者の方なので、また女性の起業家さんにも見て欲しいので、ちゃんとした雰囲気はありつつも、あまり硬くなく、自分でもできそうかなー、と思わせる様な雰囲気が出るといいなと思っています。
よろしくお願いいたします。

※著者似顔絵2点添付します。どちらかをお使いください。
※写真・イラスト素材購入の際は別途お支払いします。 その場合は、小サイズ画像で大丈夫です。

※参考資料として、まだ未完成ですが原稿を添付します。
パスワードがありますのでこちらで開いてください。

▶︎PDFを開く時のパスワード: demo1

《追記1》必ずご覧ください。
↓ ↓ ↓
書籍のタイトルとオビの文言をを変更しました。
申し訳ありませんが、こちらを必ずご確認ください。

(すでに提案をくださった方は、そのままのデザインで検討させていただきますので、再提出はしなくて大丈夫です。採用になった場合のみ変更のご依頼をさせていただきますが、その際は報酬をプラスさせていただきます※9/15日朝7時30分までに提案くださった方)

《変更内容》
<書籍タイトル>
帳簿が苦手な 店主のための
「街角で商売」

※ターゲットの目にすぐ入る様に(小さな会社)(個人事業)(ウェブに弱い)を目立つ様にお願いします。

<オビ部分>
※この本を読むまでは
ホームページは作らないでください。

▶︎参考本文(未完成)は新しい方(ファイル名:【原稿】こちらをご覧ください)
をご覧ください」
▶︎▶︎PDFファイルパスワード demo2
《追記2》
追記1にて一部変更をさせていただきましたが、
追記1の《変更内容》以外は最初の依頼内容通りなので、再度ご確認ください。

あと、少し気になったのですが、著者の似顔絵はメインビジュアルに使わなくて大丈夫です。名前の横にひっそりとつかう程度でいいかと思います。
もちろん、何か意図を持って使いたいという場合はご提案大歓迎です^ ^

▶︎必要な構成要素を再度まとめますね。
(読者ターゲットや希望デザインについては最初の依頼内容をご確認ください)
ーーーーーーーーーーーーーーーーーーー
<文字>
小さな会社や個人事業でもできる!

帳簿が苦手な 店主のための
「街角で商売」

※この本を読むまでは
ホームページは作らないでください。

読者限定プレゼント付
●思わずポチッと押したくなる!
【段階別 キャッチコピーの作り方】
●真似するだけでOK!
【ランディングページのテンプレート】

WEB集客のしくみ作りの専門家
森田 サキ

<画像>
著者似顔絵(メインビジュアルには使わなくていいいです)

※その他、写真・イラストの使用はお任せ

ーーーーーーーーーーーーーーーーーーー

こちらの説明不足のため誤解を招いてしまい、たいへん申し訳ございませんでした。

誰のための何の本ななのか、スマホでVestraを見た時でもはっきりわかるスッキリしたデザインがよかったです。また、こちらの要望通りに、ウェブが苦手な人や女性も、ついポチッと押してしまいそうなデザインでした。

選考には、20人ほどの方から意見をいただいたのですが、やはりはっきり文字が読み取れるものが人気が高かったです。
なるほどなぁ、と思ったのは、少しデザインの知識がある人(私を含め)と、とくにこだわりのない普通の人たちとでは、見る視点が違うのか、少し意見が別れました。読者目線がやはり大事ですね。

たくさんのご提案をいただき、本当にありがとうございました。

中には、さすがプロっぽいと思わせる作品や、手間をかけて作ってくださったと思われる作品もあり、本当にありがたく、また選考もかなり迷いました。

提案してくださった皆様、本当にありがとうございました。

```html
<!DOCTYPE html>
<html lang="ja">
<head>
<meta charset="utf-8">
<title>帳簿が苦手な店主のための 街角で商売</title>
<link rel="stylesheet" href="https://fonts.googleapis.com/css2?family=Noto+Sans+JP:wght@400;700;900&display=swap">
<style>
  :root {
    --yellow: #f9e35a;
    --yellow-pale: #fbeb8a;
    --ink: #1b1b1b;
    --paper: #ffffff;
    --red: #e0333c;
    --pink: #f7d4d4;
    --scene-a: #e9d6a8;
    --scene-b: #b9c9d6;
  }
  * { margin: 0; padding: 0; box-sizing: border-box; }
  html, body { width: 750px; height: 1200px; overflow: hidden; }
  body { font-family: "Noto Sans JP", sans-serif; color: var(--ink); }

  .cover {
    position: relative; width: 750px; height: 1200px; overflow: hidden;
    background: repeating-linear-gradient(90deg, var(--yellow) 0 26px, var(--yellow-pale) 26px 52px);
  }

  .headline {
    position: absolute; left: 140px; top: 14px; width: 470px;
    font-weight: 900; font-size: 64px; line-height: 1.2; text-align: center; letter-spacing: 2px;
  }
  .for-whom {
    position: absolute; left: 155px; top: 105px; width: 440px; height: 50px;
    background: var(--ink); color: var(--paper);
    font-weight: 900; font-size: 36px; line-height: 50px; text-align: center; letter-spacing: 3px;
  }

  .vertical { position: absolute; writing-mode: vertical-rl; font-weight: 900; line-height: 1; white-space: nowrap; }
  .side-left-a  { left: 14px;  top: 30px;  font-size: 56px; }
  .side-left-b  { left: 88px;  top: 235px; font-size: 44px; }
  .side-right   { left: 664px; top: 22px;  font-size: 56px; }

  .screen {
    position: absolute; left: 137px; top: 172px; width: 500px; height: 330px;
    background: var(--paper); border: 6px solid var(--ink); border-radius: 26px; z-index: 2;
  }
  .title-top {
    position: absolute; left: 0; right: 0; top: 16px; text-align: center;
    font-weight: 900; font-size: 76px; line-height: 1;
  }
  .title-roman {
    position: absolute; left: 0; right: 0; top: 98px; text-align: center;
    font-weight: 700; font-size: 17px; letter-spacing: 2px;
  }
  .title-main {
    position: absolute; left: 0; right: 0; top: 124px; text-align: center;
    font-weight: 900; font-size: 176px; line-height: 1; letter-spacing: 4px;
  }

  .scene {
    position: absolute; left: 20px; top: 505px; width: 710px; height: 440px;
    background: radial-gradient(ellipse at 50% 40%, var(--scene-a), var(--scene-b) 75%, transparent 100%);
    border-radius: 40px; z-index: 1;
  }

  .author { z-index: 3; }
  .author-portrait {
    position: absolute; left: 660px; top: 386px; width: 54px; height: 54px;
    border-radius: 50%; background: radial-gradient(circle, #f3d3bd, #8a5a3c);
    border: 3px solid var(--paper);
  }
  .author-name { left: 665px; top: 448px; font-size: 44px; letter-spacing: 4px; z-index: 3; }
  .author-role { left: 722px; top: 448px; font-size: 13px; font-weight: 700; z-index: 3; }

  .warning {
    position: absolute; left: 240px; top: 955px; width: 500px; text-align: center; z-index: 2;
  }
  .warning-lead { font-weight: 900; font-size: 46px; line-height: 1.2; white-space: nowrap; }
  .warning-body {
    display: inline-block; margin-top: 4px; padding: 2px 10px;
    background: var(--paper); font-weight: 900; font-size: 27px; line-height: 1.4; white-space: nowrap;
  }

  .gift-badge {
    position: absolute; left: 12px; top: 1052px; width: 136px; height: 136px; border-radius: 50%;
    background: var(--red); color: var(--paper); border: 4px solid var(--paper);
    display: flex; align-items: center; justify-content: center; text-align: center;
    font-weight: 900; font-size: 24px; line-height: 1.2; z-index: 2;
  }
  .gift-item { position: absolute; left: 160px; display: flex; align-items: center; gap: 10px; z-index: 2; }
  .gift-item.first { top: 1078px; }
  .gift-item.second { top: 1138px; }
  .gift-note { width: 108px; font-size: 13px; font-weight: 700; line-height: 1.3; }
  .gift-title {
    width: 460px; height: 48px; padding-left: 14px;
    background: linear-gradient(90deg, var(--paper) 85%, var(--pink));
    border: 3px solid var(--ink); border-radius: 6px;
    font-weight: 900; font-size: 25px; line-height: 42px; white-space: nowrap;
  }
</style>
</head>
<body>
<main class="cover">
  <div class="vertical side-left-a">個人事業でも</div>
  <div class="vertical side-left-b">できる!</div>
  <div class="vertical side-right">小さな会社や</div>

  <h2 class="headline">帳簿が苦手な</h2>
  <p class="for-whom">店主のための</p>

  <section class="screen">
    <h1>
      <span class="title-top">街角で</span>
      <span class="title-roman">MACHIKADO de SHOUBAI</span>
      <span class="title-main">商売</span>
    </h1>
  </section>

  <div class="scene" role="img" aria-label="ノートパソコンを囲んで喜ぶ店主たちのイラスト"></div>

  <div class="author author-portrait" role="img" aria-label="著者の似顔絵イラスト"></div>
  <p class="vertical author-name">森田 サキ</p>
  <p class="vertical author-role">WEB集客のしくみ作りの専門家</p>

  <div class="warning">
    <p class="warning-lead">この本を読むまでは</p>
    <p class="warning-body">ホームページは作らないでください。</p>
  </div>

  <div class="gift-badge">読者限定<br>プレゼント<br>付</div>
  <div class="gift-item first">
    <p class="gift-note">思わずポチッと<br>押したくなる!</p>
    <p class="gift-title">段階別 キャッチコピーの作り方</p>
  </div>
  <div class="gift-item second">
    <p class="gift-note">真似するだけで<br>OK!</p>
    <p class="gift-title">ランディングページのテンプレート</p>
  </div>
</main>
</body>
</html>
```